Environmental Engineering Site Design

http://qrvlandco.com/ is the current website that we currently have however we are looking for a new design. We are really looking for something very close to Dorvik's website. Expanding on that, we want our website to be very much like a software development company. Icon, and imagery driven with short descriptions is a plus unlike our current site. We want the site to be very clean, good subtle but power typography, and very modern. Colors we are looking to stay around a mainly blues and grays though we do value color input but please keep it toned down. Other sites that we like are:
http://www.dorvik.com/
http://www.zt-k.com/
http://www.brelowin.com/
http://oxu.com/
Industry/Entity Type
Software
Requirements
Must have
- Client login button/section somewhere, blog posts, and news.

```html
<!DOCTYPE html>
<html lang="en">
<head>
<meta charset="utf-8">
<title>Qorvane Partners – Environmental Engineering</title>
<link href="https://fonts.googleapis.com/css2?family=Source+Sans+3:wght@400;600&family=Tinos&display=swap" rel="stylesheet">
<style>
:root{
  --blue:#1a69b3;
  --blue-light:#3f97e4;
  --text:#3d3d3d;
  --muted:#6a6a6a;
  --panel-top:#ffffff;
  --panel-bottom:#e4e3e5;
  --border:#d6d6d8;
  --frame:#e8e7e9;
  --hero-a:#a9daf3;
  --hero-b:#c9e6c4;
}
*{box-sizing:border-box;margin:0;padding:0}
html,body{width:1200px;height:1147px;overflow:hidden;background:#fff}
body{position:relative;font-family:"Source Sans 3",Arial,sans-serif;color:var(--text)}
.brand{position:absolute;left:66px;top:38px;display:flex;align-items:center;gap:10px;color:var(--blue);font-size:30px;font-weight:600}
.brand-dot{width:34px;height:34px;border-radius:50%;background:var(--blue)}
.social{position:absolute;left:1034px;top:87px;display:flex;gap:10px}
.social span{width:23px;height:23px;border-radius:3px}
.social span:nth-child(1){background:#222}
.social span:nth-child(2){background:#4aa3dc}
.social span:nth-child(3){background:#2a5fa8}
.social span:nth-child(4){background:#ef7a1a}
.frame{position:absolute;left:36px;top:122px;width:1127px;height:432px;border-radius:10px;background:linear-gradient(#eeeeef,var(--frame));border:1px solid #dcdcde}
.nav{position:absolute;left:59px;top:133px;display:flex;list-style:none}
.nav li{height:41px;line-height:44px;font-size:18px;color:var(--blue);text-align:center}
.nav li.active{background:linear-gradient(var(--blue-light),var(--blue));color:#fff;border-radius:8px 8px 0 0}
.hero{position:absolute;left:39px;top:175px;width:1120px;height:377px;border-radius:8px;overflow:hidden;
  background:linear-gradient(180deg,var(--hero-a),var(--hero-b))}
.hero h1{position:absolute;left:46px;top:55px;width:700px;font-family:"Tinos","Times New Roman",serif;font-weight:400;font-size:37px;line-height:48px;color:#404040}
.panel{position:absolute;top:577px;width:338px;height:290px;border:1px solid var(--border);border-radius:7px;background:linear-gradient(var(--panel-top),var(--panel-bottom))}
.panel h2{font-weight:400;font-size:25px;color:var(--blue);margin:15px 0 0 20px}
.login{left:61px}.news{left:429px}.blog{left:797px}
.login label{display:block;font-size:17px;margin:10px 0 5px 24px}
.login .field{margin-left:22px;width:282px;height:37px;border-radius:5px;background:#fff;border:1px solid #d3d3d5;box-shadow:inset 0 2px 2px rgba(0,0,0,.15)}
.login .actions{display:flex;justify-content:space-between;align-items:center;margin:20px 35px 0 35px;font-size:15px}
.btn{width:106px;height:30px;border-radius:4px;background:linear-gradient(var(--blue-light),var(--blue));color:#fff;font-size:18px;text-align:center;line-height:30px}
.items{list-style:none;margin:18px 0 0 25px;width:290px}
.news .items li{font-size:14.5px;line-height:21px;padding:8px 0 10px;border-bottom:1px solid #fff;text-align:justify}
.news .items li:last-child{border:0}
.blog .items{margin:12px 0 0 23px;width:290px}
.blog .items li{font-size:14.5px;line-height:21px;padding:8px 0 9px;border-bottom:1px dashed #888;text-align:justify}
.more{position:absolute;right:22px;bottom:8px;font-size:13px;color:var(--blue)}
.about{position:absolute;left:67px;top:904px;width:1073px;font-size:16px;line-height:21px;text-align:justify}
.about p{margin-bottom:8px}
.about .more{position:absolute;right:4px;bottom:-20px}
.footer{position:absolute;left:36px;top:1069px;width:1129px;border-top:1px solid #cfcfd1;font-size:13px;color:var(--muted)}
.footer ul{list-style:none;display:flex;gap:30px;position:absolute;left:15px;top:17px}
.footer .copy{position:absolute;right:3px;top:17px}
</style>
</head>
<body>
<div class="brand"><span class="brand-dot"></span>Qorvane Partners</div>
<div class="social"><span></span><span></span><span></span><span></span></div>

<div class="frame"></div>
<ul class="nav">
  <li class="active" style="width:131px">Home</li>
  <li style="width:163px">About Us</li>
  <li style="width:165px">Disciplines</li>
  <li style="width:163px">Services</li>
  <li style="width:163px">Resources</li>
  <li style="width:163px">Contact</li>
</ul>
<div class="hero" role="img" aria-label="Photo placeholder: green grass field under a blue sky">
  <h1>Lorem Ipsum is simply dummy text of the printing and typesetting industry.</h1>
</div>

<section class="panel login">
  <h2>Client login</h2>
  <label>Username</label><div class="field"></div>
  <label>Password</label><div class="field"></div>
  <div class="actions"><span>Forgot Password?</span><span class="btn">Login</span></div>
</section>

<section class="panel news">
  <h2>Recent News</h2>
  <ul class="items">
    <li>Lorem Ipsum is simply dummy text of the printing and typesetting industry.</li>
    <li>Lorem Ipsum is simply dummy text of the printing and typesetting industry.</li>
    <li>Lorem Ipsum is simply dummy text of the printing and typesetting industry.</li>
  </ul>
  <span class="more">view more</span>
</section>

<section class="panel blog">
  <h2>Recent Blog Posts</h2>
  <ul class="items">
    <li>Lorem Ipsum is simply dummy text of the printing and typesetting industry.</li>
    <li>Lorem Ipsum is simply dummy text of the printing and typesetting industry.</li>
    <li>Lorem Ipsum is simply dummy text of the printing and typesetting industry.</li>
  </ul>
  <span class="more">view more</span>
</section>

<section class="about">
  <p>Qorvane Partners (QVP) is a full-service, woman-owned, environmental engineering consultancy specializing in brownfields initiatives. Headquartered in Corvell, Texas, QVP provides global environmental engineering services to both the public and private sectors.</p>
  <p>QVP has developed a multi-disciplined team of world-class environmental professionals by diligently recruiting from the top 10% of the industry's leading environmental engineers, scientists and geologists. Our clients are made up of Oil and Gas Exploration Companies, Chemical Producers, Manufacturers, Fabricators, Developers, Investors, Lenders, Brokers, Law Firms and Government Agencies.</p>
  <span class="more">read more</span>
</section>

<footer class="footer">
  <ul><li>Home</li><li>About Us</li><li>Disciplines</li><li>Services</li><li>Resources</li><li>Contact</li></ul>
  <span class="copy">Copyright 2012 qvp, All Rights Reserved</span>
</footer>
</body>
</html>
```